KTR Football Academy Flyer

Flyer for a full page of a yearbook ( dimensions below ) along with all the contents/photos for the flyer.
Width - 210 mm
Height - 297 mm
Please also see attached the previous flyer which we feel is in need of an upgrade !
Flyer will also be used on social media pages.
Creating next level athletes !
Providing a platform and the correct environment for young football players to develop and fulfil their potential.
Why choose KTR Football Academy
- Multiple programs for everyone
- WAPL qualified & experienced coaches
- Safe and fun environment
- All coaches police checked
- Coaches Emergency First Aid Qualified
- Coaches Safeguarding Children Qualified
- Develop new skills
- Make new friends
- Improve your fitness
REGISTER NOW!
www.brightfieldathletix.example
+968 912 40637
Instagram/Facebook - ktrfootballacademy

```html
<!DOCTYPE html>
<html lang="en">
<head>
<meta charset="utf-8">
<title>KTR Football Academy Flyer</title>
<link href="https://fonts.googleapis.com/css2?family=Roboto:ital,wght@0,400;0,700;0,900;1,500&display=swap" rel="stylesheet">
<style>
  :root {
    --backdrop: #e6e6e6;
    --paper: #ffffff;
    --brand-green: #86c24f;
    --ink: #111111;
    --muted: #555555;
    --bullet-ring: #3c3c3c;
  }
  * { margin: 0; padding: 0; box-sizing: border-box; }
  html, body {
    width: 1199px; height: 1200px; overflow: hidden;
    background: var(--backdrop);
    font-family: "Roboto", Arial, sans-serif;
  }
  .flyer {
    position: absolute; left: 234px; top: 82px;
    width: 732px; height: 1036px;
    background: var(--paper);
    overflow: hidden;
  }
  .flyer-shapes { position: absolute; inset: 0; width: 100%; height: 100%; }
  .academy-mark {
    position: absolute; left: 480px; top: 72px; width: 210px;
    text-align: center; color: var(--brand-green);
    font-weight: 900; font-size: 28px; line-height: 1.12; text-transform: uppercase;
  }
  .academy-mark .mark-dot {
    display: block; width: 96px; height: 96px; margin: 0 auto 16px;
    border-radius: 50%; background: var(--brand-green);
  }
  .why-choose { position: absolute; left: 40px; top: 662px; color: var(--paper); }
  .why-choose h2 { font-weight: 700; font-size: 34px; line-height: 38px; }
  .why-choose h3 { font-weight: 700; font-size: 24px; line-height: 30px; margin-top: 2px; }
  .benefits { list-style: none; position: absolute; left: 40px; top: 773px; }
  .benefits li {
    position: relative; padding-left: 23px;
    font-style: italic; font-weight: 500; font-size: 14.5px; line-height: 22.2px;
    color: var(--paper);
  }
  .benefits li::before {
    content: ""; position: absolute; left: 0; top: 6px;
    width: 11px; height: 11px; border-radius: 50%;
    background: var(--paper); border: 2px solid var(--bullet-ring);
  }
  .register {
    position: absolute; left: 505px; top: 754px; width: 200px;
    text-align: center; color: var(--ink);
    font-weight: 700; font-size: 34px; line-height: 43px;
  }
  .contact {
    position: absolute; right: 36px; top: 933px;
    text-align: right; color: var(--muted);
    font-style: normal; font-weight: 400; font-size: 14px;
  }
  .contact p { display: flex; justify-content: flex-end; align-items: center; gap: 7px; line-height: 18px; }
  .contact .social { margin-top: 13px; }
  .contact svg { width: 11px; height: 11px; fill: var(--muted); }
  .contact .plain-square { width: 10px; height: 10px; background: var(--muted); border-radius: 2px; }
</style>
</head>
<body>
  <main class="flyer">
    <svg class="flyer-shapes" viewBox="0 0 586 829" preserveAspectRatio="none">
      <defs>
        <linearGradient id="photoTones" gradientUnits="userSpaceOnUse" x1="0" y1="0" x2="0" y2="510">
          <stop offset="0" stop-color="#18211a"/>
          <stop offset="0.2" stop-color="#283129"/>
          <stop offset="0.36" stop-color="#5e4d3b"/>
          <stop offset="0.48" stop-color="#3d4740"/>
          <stop offset="0.6" stop-color="#b9bcb5"/>
          <stop offset="0.68" stop-color="#6e8b52"/>
          <stop offset="0.8" stop-color="#5f913b"/>
          <stop offset="1" stop-color="#4b7a2e"/>
        </linearGradient>
      </defs>
      <path class="match-photo" role="img"
        aria-label="Photo: two young players in green and lilac kits contesting the ball on a floodlit pitch"
        fill="url(#photoTones)"
        d="M0 0 H392 L384 20 L372 44 L362 70 L356 100 L350 130 L346 160 L356 182 L372 200 L392 222 L414 240 L440 255 L470 268 L500 275 L530 280 L560 282 L586 284 V510 L560 500 L530 494 L500 488 L470 482 L440 480 L410 484 L380 488 L350 492 L326 496 L300 502 L270 500 L240 496 L200 500 L160 498 L120 502 L80 500 L40 504 L0 506 Z"/>
      <path class="green-splash" fill="var(--brand-green)"
        d="M0 498 L40 496 L80 492 L120 494 L160 490 L200 492 L240 488 L270 492 L292 486 L302 506 L316 534 L328 562 L336 590 L350 620 L372 646 L392 668 L400 690 L388 712 L366 734 L348 756 L332 780 L318 804 L306 829 H0 Z"/>
    </svg>

    <div class="academy-mark"><span class="mark-dot"></span>KTR<br>Football Academy</div>

    <section class="why-choose">
      <h2>WHY CHOOSE</h2>
      <h3>KTR FOOTBALL ACADEMY</h3>
    </section>

    <ul class="benefits">
      <li>Multiple programs for everyone</li>
      <li>WAPL qualified &amp; experienced coaches</li>
      <li>Safe and fun environment</li>
      <li>All coaches police checked</li>
      <li>Coaches Emergency First Aid Qualified</li>
      <li>Coaches Safeguarding Children Qualified</li>
      <li>Develop new skills</li>
      <li>Make new friends</li>
      <li>Improve your fitness</li>
    </ul>

    <p class="register">REGISTER<br>NOW!</p>

    <address class="contact">
      <p>+968 912 40637
        <svg viewBox="0 0 24 24" aria-hidden="true"><path d="M6.6 10.8a15.1 15.1 0 0 0 6.6 6.6l2.2-2.2a1 1 0 0 1 1-.25 11.4 11.4 0 0 0 3.6.57 1 1 0 0 1 1 1V20a1 1 0 0 1-1 1A17 17 0 0 1 3 4a1 1 0 0 1 1-1h3.5a1 1 0 0 1 1 1c0 1.25.2 2.45.57 3.57a1 1 0 0 1-.25 1z"/></svg>
      </p>
      <p>www.brightfieldathletix.example
        <svg viewBox="0 0 24 24" aria-hidden="true"><circle cx="12" cy="12" r="10"/></svg>
      </p>
      <p class="social">ktrfootballacademy <span class="plain-square"></span></p>
    </address>
  </main>
</body>
</html>
```